2021 IT Training Presentation Deck Refresh

Copper Lantern is an IT education services firm. We teach IT industry standards and technologies. We are in need of an updated training presentation deck that factors in a fresh take for:

1) Agenda/Table of Contents
2) Chapter Topic Summary
2) Chapter Introduction and Learning Objectives
3) Chapter Recaps
4) Important Point/Pro Tip emphasis
5) Warning Message
6) Mini Quiz layout
7) Lab Exercise Introduction
7) Deck Close Out

Incorporating the official Copper Lantern colour palette for materials that will likely be used in self-paced/online recorded versions of courses.

Target Market(s)

IT

Industry/Entity Type

Computer Training

Requirements
Nice to have
• placeholder sections for images of IT workers in an office or by a computer

```html
<!DOCTYPE html>
<html lang="en">
<head>
<meta charset="utf-8">
<title>Copper Lantern – Training Deck Overview</title>
<link rel="stylesheet" href="https://fonts.googleapis.com/css2?family=Montserrat:wght@400;500;600;700;800&display=swap">
<style>
  :root{
    --brand-blue:#0b2fa5;
    --ink:#1c2233;
    --grey-text:#9aa0ab;
    --slide-bg:#f4f4f5;
    --slide-panel:#fbfbfc;
    --stage-left:#ffffff;
    --stage-right:#ebebed;
  }
  *{margin:0;padding:0;box-sizing:border-box}
  html,body{width:1200px;height:675px;overflow:hidden}
  body{font-family:'Montserrat',sans-serif;background:var(--stage-right);position:relative}
  .stage-left{position:absolute;left:0;top:0;width:428px;height:675px;background:var(--stage-left)}
  .slide{position:absolute;width:188px;height:106px;background:var(--slide-bg);box-shadow:0 1px 3px rgba(0,0,0,.08)}
  .slide.large{width:330px;height:186px;box-shadow:0 4px 14px rgba(0,0,0,.12)}
  .caption{position:absolute;left:0;width:428px;top:588px;text-align:center;font-weight:700;font-size:19px;line-height:23px;color:#111}
  .headline{position:absolute;left:484px;width:216px;top:42px;text-align:center;font-weight:700;font-size:21px;line-height:24px;color:#111}
  .blue{fill:var(--brand-blue)}
  .ink{fill:var(--ink)}
  .grey{fill:var(--grey-text)}
  .white{fill:#fff}
  .title-lg{font-size:12px;font-weight:600}
  .title-rg{font-size:12px;font-weight:400}
  .label{font-size:4.6px;font-weight:700}
  .body{font-size:3.8px;font-weight:400}
  .brand-name{font-size:5px;font-weight:600}
  .rule{stroke:var(--brand-blue);stroke-width:1}
  .panel{fill:var(--slide-panel)}
  .defs{position:absolute;width:0;height:0}
</style>
</head>
<body>
<svg class="defs" aria-hidden="true">
  <defs>
    <linearGradient id="ph-office" x1="0" y1="0" x2="1" y2="1"><stop offset="0" stop-color="#5d6c80"/><stop offset="1" stop-color="#d9dde3"/></linearGradient>
    <linearGradient id="ph-wood" x1="0" y1="0" x2="1" y2="1"><stop offset="0" stop-color="#8a7a6d"/><stop offset="1" stop-color="#c79a6a"/></linearGradient>
    <linearGradient id="ph-network" x1="0" y1="0" x2="1" y2="1"><stop offset="0" stop-color="#0d1f4e"/><stop offset="1" stop-color="#2f4a7d"/></linearGradient>
    <linearGradient id="ph-grey" x1="0" y1="0" x2="1" y2="1"><stop offset="0" stop-color="#c9c9c9"/><stop offset="1" stop-color="#5a5a5a"/></linearGradient>
    <linearGradient id="ph-ticker" x1="0" y1="0" x2="0" y2="1"><stop offset="0" stop-color="#3b2a5e"/><stop offset="1" stop-color="#7a5a2a"/></linearGradient>
    <linearGradient id="ph-flag" x1="0" y1="0" x2="1" y2="1"><stop offset="0" stop-color="#2f9a3f"/><stop offset="1" stop-color="#e0cf3a"/></linearGradient>
    <linearGradient id="ph-coin" x1="0" y1="0" x2="1" y2="1"><stop offset="0" stop-color="#3c6f8c"/><stop offset="1" stop-color="#2a3e55"/></linearGradient>
    <linearGradient id="ph-floor" x1="0" y1="0" x2="1" y2="1"><stop offset="0" stop-color="#d9b784"/><stop offset="1" stop-color="#e8c23a"/></linearGradient>
    <linearGradient id="ph-city" x1="0" y1="0" x2="1" y2="1"><stop offset="0" stop-color="#3a5fa8"/><stop offset="1" stop-color="#10204f"/></linearGradient>
    <linearGradient id="ph-portrait" x1="0" y1="0" x2="1" y2="1"><stop offset="0" stop-color="#c8c8c8"/><stop offset="1" stop-color="#3d4350"/></linearGradient>
    <linearGradient id="ph-coffee" x1="0" y1="0" x2="1" y2="1"><stop offset="0" stop-color="#3b2a22"/><stop offset="1" stop-color="#c9a27c"/></linearGradient>
    <linearGradient id="ph-desk" x1="0" y1="0" x2="1" y2="1"><stop offset="0" stop-color="#e8eaee"/><stop offset="1" stop-color="#9ba5b3"/></linearGradient>
    <linearGradient id="ph-screen" x1="0" y1="0" x2="0" y2="1"><stop offset="0" stop-color="#2a2c30"/><stop offset="1" stop-color="#8d9098"/></linearGradient>
  </defs>
</svg>

<section class="stage-left">

  <!-- Title slide -->
  <svg class="slide" style="left:22px;top:22px" viewBox="0 0 400 225">
    <polygon class="panel" points="160,0 300,0 245,85"/>
    <polygon class="panel" points="290,130 400,60 400,225 330,225"/>
    <polygon class="blue" points="0,70 145,150 118,225 0,225"/>
    <line class="rule" x1="30" y1="0" x2="128" y2="52"/>
    <text class="blue" font-size="17" transform="translate(128,56) rotate(33)"><tspan font-weight="700">TRAINING</tspan><tspan font-weight="400">TITLE</tspan></text>
    <g transform="translate(338,140) rotate(-20)">
      <rect class="blue" x="-26" y="-26" width="52" height="52"/>
      <text class="white" x="0" y="4" font-size="11" text-anchor="middle">2021</text>
    </g>
    <text class="white label" x="14" y="160">Words about this training</text>
    <text class="white body" x="14" y="178">A short summary of the</text>
    <text class="white body" x="14" y="186">course goals and outcomes</text>
  </svg>

  <!-- Agenda slide -->
  <svg class="slide" style="left:221px;top:22px" viewBox="0 0 400 225">
    <circle class="blue" cx="20" cy="20" r="3.5"/><text class="blue brand-name" x="26" y="22">Copper Lantern</text>
    <rect x="250" y="0" width="150" height="225" fill="url(#ph-network)" role="img" aria-label="Dark blue network of connected people icons"/>
    <rect class="blue" x="250" y="0" width="10" height="225"/>
    <line class="rule" x1="0" y1="55" x2="35" y2="55"/>
    <text class="blue title-rg" x="50" y="59">AGENDA</text>
    <g class="agenda-points">
      <circle cx="48" cy="85" r="3" fill="none" stroke="#b7bcc6" stroke-width=".8"/><text class="ink label" x="54" y="87">First Point</text><text class="grey body" x="50" y="97">Brief note on this topic</text>
      <circle cx="146" cy="85" r="3" fill="none" stroke="#b7bcc6" stroke-width=".8"/><text class="ink label" x="152" y="87">Second Point</text><text class="grey body" x="148" y="97">Brief note on this topic</text>
      <circle cx="48" cy="133" r="3" fill="none" stroke="#b7bcc6" stroke-width=".8"/><text class="ink label" x="54" y="135">Third Point</text><text class="grey body" x="50" y="145">Brief note on this topic</text>
      <circle cx="146" cy="133" r="3" fill="none" stroke="#b7bcc6" stroke-width=".8"/><text class="ink label" x="152" y="135">Fourth Point</text><text class="grey body" x="148" y="145">Brief note on this topic</text>
    </g>
    <g class="corner-mark"><rect class="blue" x="0" y="208" width="8" height="8"/><rect class="blue" x="8" y="200" width="6" height="6"/><rect class="blue" x="12" y="214" width="6" height="6"/></g>
  </svg>

  <!-- Chapter 1 slide -->
  <svg class="slide" style="left:22px;top:137px" viewBox="0 0 400 225">
    <polygon class="panel" points="0,80 0,0 245,0 105,225 60,225"/>
    <polygon class="blue" points="195,225 250,160 340,225"/>
    <text class="blue" x="220" y="108" font-size="15" font-weight="600">CHAPTER 1</text>
    <line class="rule" x1="325" y1="102" x2="400" y2="102"/>
    <text class="grey" x="220" y="124" font-size="6">Nice intro sentence to the chapter.</text>
    <g class="corner-mark"><rect class="blue" x="0" y="208" width="8" height="8"/><rect class="blue" x="8" y="200" width="6" height="6"/><rect class="blue" x="12" y="214" width="6" height="6"/></g>
  </svg>

  <!-- Chapter introduction slide -->
  <svg class="slide" style="left:221px;top:137px" viewBox="0 0 400 225">
    <circle class="blue" cx="20" cy="20" r="3.5"/><text class="blue brand-name" x="26" y="22">Copper Lantern</text>
    <rect x="0" y="35" width="192" height="73" fill="url(#ph-office)" role="img" aria-label="Team at a desk reviewing printed charts"/>
    <rect x="200" y="35" width="200" height="73" fill="url(#ph-wood)" role="img" aria-label="Hand placing a wooden block on a stacked tower"/>
    <line class="rule" x1="0" y1="145" x2="65" y2="145"/>
    <text class="blue title-lg" x="78" y="149" font-size="11">CHAPTER</text>
    <text class="ink title-rg" x="78" y="164" font-size="11">INTRODUCTION</text>
    <text class="grey body" x="218" y="143">Key context for this chapter</text>
    <text class="grey body" x="218" y="150">and why it matters.</text>
    <text class="grey body" x="218" y="163">What you will learn and</text>
    <text class="grey body" x="218" y="170">practise in this part.</text>
    <g class="corner-mark"><rect class="blue" x="0" y="208" width="8" height="8"/><rect class="blue" x="8" y="200" width="6" height="6"/><rect class="blue" x="12" y="214" width="6" height="6"/></g>
  </svg>

  <!-- Key learnings of the chapter slide -->
  <svg class="slide" style="left:22px;top:250px" viewBox="0 0 400 225">
    <circle class="blue" cx="20" cy="20" r="3.5"/><text class="blue brand-name" x="26" y="22">Copper Lantern</text>
    <rect x="110" y="42" width="90" height="138" fill="url(#ph-desk)" role="img" aria-label="Colleagues discussing charts at a desk"/>
    <rect class="blue" x="35" y="42" width="70" height="66"/>
    <g stroke="#fff" stroke-width=".8" fill="#fff"><circle cx="67" cy="57" r="1.3"/><circle cx="73" cy="54" r="1.3"/><circle cx="73" cy="60" r="1.3"/><line x1="67" y1="57" x2="73" y2="54"/><line x1="67" y1="57" x2="73" y2="60"/></g>
    <text class="white label" x="70" y="74" text-anchor="middle">Blabla</text>
    <text class="white body" x="70" y="88" text-anchor="middle">Short card note</text>
    <rect x="35" y="115" width="70" height="65" fill="#fff"/>
    <text class="ink label" x="70" y="135" text-anchor="middle">100%</text>
    <text class="blue body" x="70" y="143" text-anchor="middle">KPI</text>
    <text class="grey body" x="70" y="157" text-anchor="middle">Short card note</text>
    <text class="blue title-lg" x="230" y="68" font-size="11">KEY LEARNINGS</text>
    <line class="rule" x1="342" y1="63" x2="400" y2="63"/>
    <text class="ink title-rg" x="230" y="82" font-size="11">OF THE CHAPTER</text>
    <text class="grey body" x="230" y="115">Main takeaway from this chapter</text>
    <text class="grey body" x="230" y="122">in a few words.</text>
    <text class="grey body" x="230" y="135">A second takeaway to remember</text>
    <text class="grey body" x="230" y="142">for later.</text>
    <g class="corner-mark"><rect class="blue" x="0" y="208" width="8" height="8"/><rect class="blue" x="8" y="200" width="6" height="6"/><rect class="blue" x="12" y="214" width="6" height="6"/></g>
  </svg>

  <!-- Mini quiz slide -->
  <svg class="slide" style="left:221px;top:250px" viewBox="0 0 400 225">
    <circle class="blue" cx="20" cy="20" r="3.5"/><text class="blue brand-name" x="26" y="22">Copper Lantern</text>
    <rect class="blue" x="315" y="0" width="85" height="225"/>
    <rect x="205" y="35" width="75" height="165" fill="url(#ph-ticker)" role="img" aria-label="Stock ticker board with prices"/>
    <rect x="285" y="35" width="93" height="90" fill="url(#ph-flag)" stroke="#fff" stroke-width="2" role="img" aria-label="Waving national flag"/>
    <rect x="285" y="133" width="65" height="67" fill="url(#ph-coin)" stroke="#fff" stroke-width="2" role="img" aria-label="Close-up of a coin"/>
    <line class="rule" x1="0" y1="52" x2="35" y2="52"/>
    <text class="blue title-lg" x="50" y="58" font-size="11">MINI</text>
    <text class="ink title-lg" x="50" y="72" font-size="11">QUIZ</text>
    <text class="ink label" x="50" y="92">QUESTION: Which standard covers</text>
    <text class="ink label" x="50" y="101">the topic from this chapter and</text>
    <text class="ink label" x="50" y="110">when is it applied?</text>
    <g class="quiz-options">
      <polyline points="50,132 53,135 50,138" fill="none" stroke="var(--brand-blue)" stroke-width="1"/><text class="blue label" x="60" y="134">First Option</text><text class="grey body" x="60" y="142">Short answer detail here</text>
      <polyline points="50,162 53,165 50,168" fill="none" stroke="var(--brand-blue)" stroke-width="1"/><text class="blue label" x="60" y="164">Second Option</text><text class="grey body" x="60" y="172">Short answer detail here</text>
      <polyline points="50,192 53,195 50,198" fill="none" stroke="var(--brand-blue)" stroke-width="1"/><text class="blue label" x="60" y="194">Third Option</text><text class="grey body" x="60" y="202">Short answer detail here</text>
    </g>
    <g class="corner-mark"><rect class="blue" x="0" y="208" width="8" height="8"/><rect class="blue" x="8" y="200" width="6" height="6"/><rect class="blue" x="12" y="214" width="6" height="6"/></g>
  </svg>

  <!-- Key learnings slide -->
  <svg class="slide" style="left:22px;top:364px" viewBox="0 0 400 225">
    <circle class="blue" cx="20" cy="20" r="3.5"/><text class="blue brand-name" x="26" y="22">Copper Lantern</text>
    <rect x="0" y="40" width="195" height="80" fill="url(#ph-grey)" stroke="#fff" stroke-width="3" role="img" aria-label="Black and white group of raised hands"/>
    <text class="blue title-lg" x="220" y="68" font-size="11">KEY</text>
    <line class="rule" x1="245" y1="63" x2="400" y2="63"/>
    <text class="ink title-lg" x="220" y="83" font-size="11">LEARNINGS</text>
    <rect class="blue" x="50" y="140" width="1.2" height="7"/><text class="ink label" x="55" y="146">FIRST POINT</text>
    <text class="grey body" x="50" y="158">Explain the first point in</text>
    <text class="grey body" x="50" y="165">one or two lines.</text>
    <rect class="blue" x="215" y="140" width="1.2" height="7"/><text class="ink label" x="220" y="146">SECOND POINT</text>
    <text class="grey body" x="215" y="158">Explain the second point in</text>
    <text class="grey body" x="215" y="165">one or two lines.</text>
    <g class="corner-mark"><rect class="blue" x="0" y="208" width="8" height="8"/><rect class="blue" x="8" y="200" width="6" height="6"/><rect class="blue" x="12" y="214" width="6" height="6"/></g>
  </svg>

  <!-- Warning slide -->
  <svg class="slide" style="left:221px;top:364px" viewBox="0 0 400 225">
    <circle class="blue" cx="20" cy="20" r="3.5"/><text class="blue brand-name" x="26" y="22">Copper Lantern</text>
    <polygon class="blue" points="140,0 320,0 230,88"/>
    <polygon points="212,120 330,35 400,95 400,225 300,225" fill="url(#ph-floor)" stroke="#fff" stroke-width="3" role="img" aria-label="Yellow wet floor sign on a wooden floor"/>
    <line class="rule" x1="0" y1="52" x2="35" y2="52"/>
    <text class="blue title-lg" x="50" y="57" font-size="11">WARNING</text>
    <text class="grey body" x="50" y="100">Describe the risk and how learners</text>
    <text class="grey body" x="50" y="107">can avoid it.</text>
    <text class="grey body" x="50" y="142">Add the safe way to proceed</text>
    <text class="grey body" x="50" y="149">in this step.</text>
    <g class="corner-mark"><rect class="blue" x="0" y="208" width="8" height="8"/><rect class="blue" x="8" y="200" width="6" height="6"/><rect class="blue" x="12" y="214" width="6" height="6"/></g>
  </svg>

  <!-- Lab exercise slide -->
  <svg class="slide" style="left:22px;top:478px" viewBox="0 0 400 225">
    <circle class="blue" cx="20" cy="20" r="3.5"/><text class="blue brand-name" x="26" y="22">Copper Lantern</text>
    <circle class="blue" cx="317" cy="112" r="82"/>
    <rect x="205" y="55" width="165" height="122" fill="url(#ph-screen)" role="img" aria-label="Desktop computer monitor"/>
    <line class="rule" x1="0" y1="64" x2="38" y2="64"/>
    <text class="blue title-rg" x="50" y="68" font-size="11">LAB</text>
    <text class="ink title-rg" x="50" y="82" font-size="11">EXERCISE</text>
    <text class="grey body" x="50" y="116">Set up the lab and follow</text>
    <text class="grey body" x="50" y="123">each step.</text>
    <text class="grey body" x="50" y="156">Check results before moving on.</text>
    <g class="corner-mark"><rect class="blue" x="0" y="208" width="8" height="8"/><rect class="blue" x="8" y="200" width="6" height="6"/><rect class="blue" x="12" y="214" width="6" height="6"/></g>
  </svg>

  <!-- Thank you slide -->
  <svg class="slide" style="left:221px;top:478px" viewBox="0 0 400 225">
    <circle class="blue" cx="20" cy="20" r="3.5"/><text class="blue brand-name" x="26" y="22">Copper Lantern</text>
    <polygon points="180,0 400,0 400,225 100,225 255,110" fill="url(#ph-city)" role="img" aria-label="City skyline at dusk in blue tones"/>
    <line class="rule" x1="0" y1="86" x2="38" y2="86"/>
    <text class="blue title-lg" x="50" y="90" font-size="12">THANK YOU</text>
    <text class="grey body" x="50" y="143">Closing note for the learners.</text>
    <text class="white body" x="318" y="202">Website</text>
    <text class="white body" x="318" y="210">www.lanternlearn.net</text>
    <g class="corner-mark"><rect class="blue" x="0" y="208" width="8" height="8"/><rect class="blue" x="8" y="200" width="6" height="6"/><rect class="blue" x="12" y="214" width="6" height="6"/></g>
  </svg>

  <p class="caption">Fully customizable slide deck<br>All pictures to be customized<br>20+ different set up included</p>
</section>

<h1 class="headline">All pictures are for illustration purpose only</h1>

<!-- Welcome message slide -->
<svg class="slide large" style="left:474px;top:160px" viewBox="0 0 400 225">
  <circle class="blue" cx="20" cy="20" r="3.5"/><text class="blue brand-name" x="26" y="22">Copper Lantern</text>
  <rect x="230" y="0" width="150" height="225" fill="url(#ph-portrait)" role="img" aria-label="Portrait of a smiling presenter in a suit"/>
  <rect class="blue" x="380" y="0" width="20" height="225"/>
  <rect class="blue" x="212" y="120" width="50" height="32"/>
  <text class="white label" x="220" y="133">Name</text>
  <text class="white body" x="220" y="142">Role</text>
  <line class="rule" x1="0" y1="56" x2="38" y2="56"/>
  <text class="blue title-lg" x="50" y="60" font-size="11">WELCOME</text>
  <text class="ink title-rg" x="50" y="74" font-size="11">MESSAGE</text>
  <text class="grey body" x="50" y="100">A short welcome note from</text>
  <text class="grey body" x="50" y="107">the course lead.</text>
  <g class="corner-mark"><rect class="blue" x="0" y="208" width="8" height="8"/><rect class="blue" x="8" y="200" width="6" height="6"/><rect class="blue" x="12" y="214" width="6" height="6"/></g>
</svg>

<!-- About the chapter slide -->
<svg class="slide large" style="left:824px;top:160px" viewBox="0 0 400 225">
  <circle class="blue" cx="20" cy="20" r="3.5"/><text class="blue brand-name" x="26" y="22">Copper Lantern</text>
  <rect x="248" y="30" width="72" height="95" fill="url(#ph-coin)" stroke="#fff" stroke-width="2" role="img" aria-label="Rows of solar panels under a clear sky"/>
  <rect x="325" y="30" width="75" height="72" fill="url(#ph-desk)" stroke="#fff" stroke-width="2" role="img" aria-label="Desk with laptop and printed charts"/>
  <line class="rule" x1="0" y1="56" x2="38" y2="56"/>
  <text class="blue title-lg" x="50" y="60" font-size="11">ABOUT THE</text>
  <text class="ink title-rg" x="50" y="74" font-size="11">CHAPTER</text>
  <polyline points="50,98 53,95 56,98" fill="none" stroke="var(--brand-blue)" stroke-width="1"/>
  <text class="ink label" x="62" y="99">First key learning</text>
  <text class="grey body" x="62" y="107">Short detail line</text>
  <polyline points="50,128 53,125 56,128" fill="none" stroke="var(--brand-blue)" stroke-width="1"/>
  <text class="ink label" x="62" y="129">Second key learning</text>
  <text class="grey body" x="62" y="137">Short detail line</text>
  <g class="corner-mark"><rect class="blue" x="0" y="208" width="8" height="8"/><rect class="blue" x="8" y="200" width="6" height="6"/><rect class="blue" x="12" y="214" width="6" height="6"/></g>
</svg>

<!-- Chapter 1 slide with photo -->
<svg class="slide large" style="left:474px;top:380px" viewBox="0 0 400 225">
  <polygon points="0,70 110,0 175,95 60,170 0,140" fill="url(#ph-desk)" stroke="#fff" stroke-width="3" role="img" aria-label="Calculator and tablet on a desk"/>
  <polygon class="blue" points="195,225 250,160 340,225"/>
  <text class="blue" x="220" y="108" font-size="15" font-weight="600">CHAPTER 1</text>
  <line class="rule" x1="325" y1="102" x2="400" y2="102"/>
  <text class="grey" x="220" y="124" font-size="6">Nice intro sentence to the chapter.</text>
  <g class="corner-mark"><rect class="blue" x="0" y="208" width="8" height="8"/><rect class="blue" x="8" y="200" width="6" height="6"/><rect class="blue" x="12" y="214" width="6" height="6"/></g>
</svg>

<!-- Break slide -->
<svg class="slide large" style="left:824px;top:380px" viewBox="0 0 400 225">
  <polygon points="0,75 120,20 185,150 60,205 0,185" fill="url(#ph-coffee)" stroke="#fff" stroke-width="3" role="img" aria-label="Hands holding cups of latte coffee"/>
  <polygon class="blue" points="205,225 250,165 340,225"/>
  <text class="blue" x="225" y="100" font-size="15" font-weight="600">BREAK</text>
  <line class="rule" x1="290" y1="94" x2="400" y2="94"/>
  <text class="grey" x="300" y="112" font-size="5">Back at 3:30 PM</text>
  <g class="corner-mark"><rect class="blue" x="0" y="208" width="8" height="8"/><rect class="blue" x="8" y="200" width="6" height="6"/><rect class="blue" x="12" y="214" width="6" height="6"/></g>
</svg>
</body>
</html>
```